Website for a Steadwell, an HVAC company.

We are a company that provides residential and commercial service. We don’t need any widgets other than a call to action where customers can message us. Though we have very few google reviews, they are all great and would like to see those populated. Simple and modern is the style. I included our logo and a pic of our vans.

Target Market(s)

Residential customers

Coding

Number of Pages Required

1 page

Font styles to use
Sans Serif

Colors
0054AA
0677BA
7BADD7
CADEEF
E8F1F8
EE7325
F08F49
F5BC92
FAE3D3
FDF4ED

```html
<!DOCTYPE html>
<html lang="en">
<head>
<meta charset="utf-8">
<title>Steadwell Heating and Air</title>
<link rel="stylesheet" href="https://fonts.googleapis.com/css2?family=Ubuntu:wght@400;500;700&family=Lato:wght@400;700&display=swap">
<style>
:root{
  --blue-dark:#0054AA;
  --blue:#0677BA;
  --blue-mid:#3F7ED6;
  --blue-light:#7BADD7;
  --blue-pale:#CADEEF;
  --blue-mist:#E8F1F8;
  --orange:#EE7325;
  --orange-soft:#F08F49;
  --orange-pale:#F5BC92;
  --ink:#1b1b1b;
  --text:#444;
  --navy:#0d1424;
  --white:#fff;
}
*{box-sizing:border-box;margin:0;padding:0}
html,body{width:1200px;height:4910px;overflow:hidden}
body{font-family:"Lato",sans-serif;color:var(--text);background:var(--white);position:relative}
h1,h2,h3{font-family:"Ubuntu",sans-serif;font-weight:400;color:var(--ink)}
.accent{color:var(--blue-mid);font-weight:500}
.btn{display:inline-block;background:var(--orange);color:var(--white);font-family:"Lato",sans-serif;font-weight:700;font-size:15px;border-radius:3px;text-align:center}
.ph{position:absolute}

/* header */
.topbar{position:absolute;top:0;height:22px;background:var(--blue);color:var(--white);font-size:11px;line-height:22px}
.topbar.left{left:0;width:520px;padding-left:118px}
.topbar.right{right:0;width:520px;text-align:right;padding-right:120px}
.logo-badge{position:absolute;left:500px;top:-60px;width:200px;height:200px;border-radius:50%;background:var(--white);box-shadow:0 4px 10px rgba(0,0,0,.15);z-index:3;text-align:center}
.logo-badge .dot{width:44px;height:44px;border-radius:50%;background:var(--orange);margin:82px auto 8px}
.logo-badge .name{font-family:"Ubuntu",sans-serif;font-weight:700;font-size:17px;letter-spacing:2px;color:var(--blue-dark)}
.nav{position:absolute;top:50px;left:110px;display:flex;gap:22px;font-size:12px;color:#333}
.nav .active{color:var(--blue)}
.call{position:absolute;top:42px;left:748px;display:flex;align-items:center;gap:12px;color:var(--orange);font-size:17px}
.call .ico{width:26px;height:26px;border-radius:50%;background:var(--orange-pale);display:flex;align-items:center;justify-content:center}
.book{position:absolute;left:977px;top:34px;width:116px;height:38px;line-height:38px}

/* hero */
.hero{position:absolute;top:84px;left:0;width:1200px;height:620px;background:linear-gradient(120deg,#d9c8b2,#efe6da 45%,#c9b49a);}
.hero-title{position:absolute;top:340px;left:0;width:1200px;text-align:center;font-family:"Ubuntu",sans-serif;font-weight:700;font-size:60px;color:var(--white);text-shadow:0 3px 8px rgba(0,0,0,.45)}
.hero-btn{position:absolute;left:475px;top:423px;width:250px;height:40px;line-height:40px;background:var(--blue-mid);color:var(--white);border-radius:4px;font-size:15px;text-align:center}
.hero-curve{position:absolute;left:0;top:560px}

/* about */
.about h2{position:absolute;left:110px;top:780px;font-size:40px;line-height:54px}
.about p{position:absolute;left:106px;top:905px;width:560px;font-size:13px;line-height:36px;color:#333}
.about .btn{position:absolute;left:112px;top:1066px;width:142px;height:38px;line-height:38px}
.about-photo{left:724px;top:798px;width:362px;height:362px;border-radius:50%;background:radial-gradient(circle at 40% 40%,#c8543f,#8a3a2c 50%,#3b4a68);}

/* industries */
.ind{position:absolute;top:1215px;left:0;width:1200px;height:580px}
.ind-title{position:absolute;left:373px;top:1215px;width:457px;height:72px;background:var(--white);border-radius:0 0 18px 18px;text-align:center;font-size:40px;line-height:60px;z-index:2}
.ind-label{position:absolute;top:1712px;font-family:"Ubuntu",sans-serif;font-weight:500;font-size:40px;color:var(--white);text-shadow:0 2px 6px rgba(0,0,0,.5)}

/* services */
.what h2{position:absolute;top:1870px;left:0;width:1200px;text-align:center;font-size:42px;font-weight:500}
.card{position:absolute;top:1950px;height:382px;background:var(--white);border-radius:8px;box-shadow:0 2px 10px rgba(0,0,0,.15);overflow:hidden}
.card .pic{position:absolute;left:10px;top:12px;right:10px;height:260px;border-radius:4px}
.card .cap{position:absolute;left:0;right:0;top:300px;text-align:center;font-family:"Ubuntu",sans-serif;font-size:22px;color:#222}
.card.feature .panel{position:absolute;left:0;top:0;right:0;height:330px;background:var(--blue-mid);border-radius:8px 8px 46px 46px}
.card.feature h3{position:absolute;top:70px;left:0;right:0;text-align:center;color:var(--white);font-size:22px;font-weight:700}
.card.feature p{position:absolute;top:108px;left:28px;right:28px;text-align:center;color:var(--white);font-size:16px;line-height:30px}
.card.feature .btn{position:absolute;left:102px;top:214px;width:114px;height:34px;line-height:34px;font-size:14px}
.card.feature .badge{position:absolute;left:94px;top:280px;width:132px;height:132px;border-radius:50%;background:var(--white);display:flex;justify-content:center;padding-top:24px}
.arrow{position:absolute;top:2139px;width:20px;height:20px;border-radius:50%;display:flex;align-items:center;justify-content:center}

/* why */
.why-photo{left:0;top:2420px;width:593px;height:593px;background:linear-gradient(160deg,#f2f2f2,#d9d9d9 60%,#bfc4ca)}
.why{position:absolute;left:593px;top:2420px;width:607px;height:593px;background:var(--blue-mid);color:var(--white)}
.why h2{position:absolute;left:45px;top:64px;color:var(--white);font-size:40px;line-height:52px;font-weight:500}
.why p{position:absolute;left:52px;top:176px;width:450px;font-size:12.5px;line-height:23px}
.feat{position:absolute;display:flex;align-items:center;gap:16px;font-size:15px;font-weight:700}
.feat .ring{width:86px;height:86px;border-radius:50%;background:var(--white);display:flex;align-items:center;justify-content:center}
.feat .ring span{width:72px;height:72px;border-radius:50%;background:var(--orange);display:flex;align-items:center;justify-content:center}

/* reviews */
.reviews h2{position:absolute;left:112px;top:3090px;font-size:40px}
.rv-nav{position:absolute;top:3098px;width:20px;height:20px;border-radius:50%}
.review{position:absolute;top:3188px;width:460px}
.review .avatar{position:absolute;left:0;top:0;width:82px;height:82px;border-radius:50%;background:linear-gradient(150deg,#c9d3dc,#8aa0b5)}
.review .who{position:absolute;left:108px;top:18px;font-size:17px;color:#222}
.review .stars{position:absolute;left:108px;top:42px;display:flex;align-items:center;gap:6px;color:var(--orange);font-size:20px;letter-spacing:1px}
.review .stars .g{width:18px;height:18px;border-radius:50%;background:var(--blue-mid)}
.review .quote{position:absolute;right:0;top:28px;font-family:"Ubuntu",sans-serif;font-weight:700;font-size:60px;line-height:60px;color:var(--blue-mid)}
.review p{position:absolute;left:0;top:110px;width:460px;font-size:12.5px;line-height:26px;color:#333}
.divider{position:absolute;left:600px;top:3215px;height:150px;border-left:2px dashed #ccc}

/* contact */
.van{left:560px;top:3536px;width:640px;height:574px;background:linear-gradient(135deg,#29405e,#101a2c 55%,#4a6a8f)}
.contact-bg{position:absolute;left:0;top:3536px;width:560px;height:574px;background:linear-gradient(135deg,#46607f,#23344c)}
.tab{position:absolute;left:560px;top:3500px;width:0;height:0;border-left:44px solid var(--orange);border-top:36px solid transparent}
.form{position:absolute;left:53px;top:3500px;width:507px;height:620px;background:var(--white);box-shadow:0 4px 16px rgba(0,0,0,.18)}
.form h2{position:absolute;left:54px;top:66px;font-size:40px}
.field{position:absolute;left:33px;width:444px;height:54px;border:1px solid #c8c8c8;border-radius:4px;box-shadow:0 2px 4px rgba(0,0,0,.12);font-size:12px;color:#555;padding:0 20px;display:flex;align-items:center;justify-content:space-between}
.form .btn{position:absolute;left:185px;top:504px;width:115px;height:40px;line-height:40px;font-size:14px}

/* brands */
.brands h2{position:absolute;top:4190px;left:0;width:1200px;text-align:center;font-size:40px;line-height:52px}
.brand{position:absolute;top:4352px;height:46px;display:flex;align-items:center;gap:10px;font-family:"Ubuntu",sans-serif;font-weight:700;white-space:nowrap}
.brand i{display:block;flex:none;width:40px;height:40px;border-radius:50%}
.brand.norvale{left:104px;font-size:28px;color:#d0312d}
.brand.kestrel{left:352px;font-size:20px;color:#d0312d}
.brand.brightline{left:502px;font-size:20px;color:#c8272c}
.brand.halvor{left:722px;font-size:24px;color:#333}
.brand.teloric{left:910px;font-size:26px;color:#e3262b}

/* footer */
.footer{position:absolute;left:0;top:4480px;width:1200px;height:430px}
.f-logo{position:absolute;left:118px;top:4650px;width:215px;text-align:center}
.f-logo .dot{width:72px;height:72px;border-radius:50%;background:var(--orange);margin:0 auto 14px}
.f-logo .name{font-family:"Ubuntu",sans-serif;font-weight:700;font-size:22px;letter-spacing:3px;color:var(--blue-light)}
.f-logo .social{width:28px;height:28px;border-radius:50%;border:2px solid var(--blue-light);margin:18px auto 0}
.f-col{position:absolute;top:4630px;color:var(--white);font-size:12.5px}
.f-col h4{font-family:"Ubuntu",sans-serif;font-weight:500;font-size:16px;color:var(--blue-light);margin-bottom:14px}
.f-col li{list-style:none;line-height:26px}
.f-col .ci{display:flex;align-items:center;gap:14px;line-height:34px}
.f-col .ci b{width:16px;height:16px;border-radius:50%;background:var(--white);display:inline-block}
.f-rule{position:absolute;left:110px;top:4867px;width:980px;border-top:1px solid #3a4254}
.copy{position:absolute;top:4882px;left:0;width:1200px;text-align:center;color:var(--white);font-size:13px}
.chat{position:absolute;left:1048px;top:4782px;width:50px;height:50px;border-radius:50%;background:var(--white);display:flex;align-items:center;justify-content:center}
</style>
</head>
<body>

<header>
  <div class="topbar left">Welcome To Steadwell Heat And Air.....</div>
  <div class="topbar right">Serving Charleston, SC, and Surrounding Areas</div>
  <div class="logo-badge"><div class="dot"></div><div class="name">STEADWELL</div></div>
  <nav class="nav"><span class="active">Home</span><span>Services</span><span>About Us</span><span>Reviews</span><span>Contact Us</span></nav>
  <div class="call"><span class="ico"><svg width="14" height="14" viewBox="0 0 24 24"><path fill="#EE7325" d="M6.6 10.8a15.1 15.1 0 006.6 6.6l2.2-2.2c.3-.3.7-.4 1-.2 1.1.4 2.3.6 3.6.6.6 0 1 .4 1 1V20c0 .6-.4 1-1 1A17 17 0 013 4c0-.6.4-1 1-1h3.5c.6 0 1 .4 1 1 0 1.3.2 2.5.6 3.6.1.3 0 .7-.2 1z"/></svg></span>(555) 014-2290</div>
  <span class="btn book">Book Online</span>
</header>

<section>
  <div class="hero" role="img" aria-label="Smiling woman relaxing on a sofa holding an air conditioner remote"></div>
  <h1 class="hero-title">Your Comfort is our Mission</h1>
  <span class="hero-btn">Contact Us For a Free Estimate</span>
  <svg class="hero-curve" width="1200" height="170" viewBox="0 0 1200 170">
    <path d="M0 30 Q600 150 1200 50 L1200 170 L0 170Z" fill="#fff"/>
    <path d="M210 105 Q600 155 1010 90" fill="none" stroke="#29a3dd" stroke-width="9" stroke-linecap="round"/>
  </svg>
</section>

<section class="about">
  <h2>Heating and Air Conditioning<br><span class="accent">Services You Can Depend On</span></h2>
  <p>Since 2003, Steadwell Heating and Air has provided reliable and affordable heating and cooling solutions in Charleston, SC, and the surrounding areas. With over 20 years of experience, we have earned the trust of our community by delivering top-notch HVAC services. Contact us today at (555) 014-2290.</p>
  <span class="btn">Contact Us Now</span>
  <div class="ph about-photo" role="img" aria-label="Technician in a red cap servicing an outdoor AC unit"></div>
</section>

<section>
  <svg class="ind" width="1200" height="580" viewBox="0 0 1200 580">
    <polygon points="0,0 657,0 562,580 0,580" fill="#6d6a66" role="img" aria-label="Technician installing a wall unit while a couple watches in their kitchen"/>
    <polygon points="670,0 1200,0 1200,580 575,580" fill="#4f7096" role="img" aria-label="Technician in hard hat testing commercial rooftop units"/>
  </svg>
  <h2 class="ind-title">industries <span class="accent">We Serve</span></h2>
  <span class="ind-label" style="left:86px">Residential&nbsp; Service</span>
  <span class="ind-label" style="left:694px">Commercial&nbsp; Service</span>
</section>

<section class="what">
  <h2>What <span class="accent">We Do</span></h2>
  <span class="arrow" style="left:43px;background:var(--blue-mid)"><svg width="8" height="10"><path d="M6 1L2 5l4 4" stroke="#fff" stroke-width="2" fill="none"/></svg></span>
  <span class="arrow" style="left:1138px;background:#9a9a9a"><svg width="8" height="10"><path d="M2 1l4 4-4 4" stroke="#fff" stroke-width="2" fill="none"/></svg></span>
  <div class="card" style="left:110px;width:320px"><div class="pic" role="img" aria-label="Technician repairing a heating system" style="background:linear-gradient(135deg,#a4553f,#5b4a3f)"></div><div class="cap">Heating Repair</div></div>
  <div class="card feature" style="left:440px;width:318px">
    <div class="panel"></div>
    <h3>Heating Maintenance</h3>
    <p>We inspect various components, fine-tune system settings, and check for potential issues.</p>
    <span class="btn">Book Online</span>
    <div class="badge"><svg width="50" height="44" viewBox="0 0 50 44"><path d="M15 16a10 10 0 0120 0z" fill="#3F7ED6"/><rect x="3" y="18" width="44" height="6" fill="#3F7ED6"/><rect x="3" y="27" width="44" height="4" fill="#3F7ED6"/><rect x="3" y="34" width="44" height="4" fill="#3F7ED6"/></svg></div>
  </div>
  <div class="card" style="left:768px;width:318px"><div class="pic" role="img" aria-label="Technician in red repairing an outdoor AC unit" style="background:linear-gradient(135deg,#8c4a3a,#c23a33 60%,#6b6b6b)"></div><div class="cap">Ac Repair</div></div>
</section>

<section>
  <div class="ph why-photo" role="img" aria-label="Technician on a ladder installing a wall-mounted AC unit"></div>
  <div class="why">
    <h2>Why Choose Steadwell<br>Heating and Air?</h2>
    <p>Steadwell Heating and Air is more than just an HVAC company; we're your partners in creating a comfortable living environment.</p>
    <div class="feat" style="left:45px;top:276px"><span class="ring"><span><svg width="34" height="34" viewBox="0 0 24 24"><circle cx="12" cy="12" r="9" fill="none" stroke="#fff" stroke-width="2"/><path d="M8 12l3 3 5-6" stroke="#fff" stroke-width="2" fill="none"/></svg></span></span>Quality Service</div>
    <div class="feat" style="left:292px;top:276px"><span class="ring"><span><svg width="34" height="34" viewBox="0 0 24 24"><circle cx="12" cy="10" r="7" fill="none" stroke="#fff" stroke-width="2"/><path d="M12 6v8M6 21h12" stroke="#fff" stroke-width="2"/></svg></span></span>Affordability</div>
    <div class="feat" style="left:45px;top:410px"><span class="ring"><span><svg width="34" height="34" viewBox="0 0 24 24"><path d="M4 8l2 1 2-1-1 2 1 2-2-1-2 1 1-2zM10 6l2 1 2-1-1 2 1 2-2-1-2 1 1-2zM16 8l2 1 2-1-1 2 1 2-2-1-2 1 1-2z" fill="#fff"/><path d="M6 16a6 5 0 0012 0" stroke="#fff" stroke-width="2" fill="none"/></svg></span></span>Customer<br>Satisfaction</div>
    <div class="feat" style="left:292px;top:410px"><span class="ring"><span><svg width="34" height="34" viewBox="0 0 24 24"><circle cx="12" cy="8" r="3" fill="#fff"/><circle cx="5" cy="10" r="2.2" fill="#fff"/><circle cx="19" cy="10" r="2.2" fill="#fff"/><path d="M6 20a6 6 0 0112 0zM1 19a4 4 0 016-3M23 19a4 4 0 00-6-3" fill="#fff"/></svg></span></span>Community Focus</div>
  </div>
</section>

<section class="reviews">
  <h2>Customer <span class="accent">Reviews</span></h2>
  <span class="rv-nav" style="left:1038px;background:var(--blue-mid)"></span>
  <span class="rv-nav" style="left:1064px;background:#bbb"></span>
  <article class="review" style="left:110px">
    <div class="avatar" role="img" aria-label="Reviewer portrait"></div>
    <div class="who">Marla P</div>
    <div class="stars"><span class="g"></span>★★★★★</div>
    <div class="quote">&rdquo;</div>
    <p>This was my first time using Steadwell Heating and Air and I was extremely impressed with the prompt service and fair pricing. As a property manager, I work with a lot of contractors and those are two things that can be hard to find. I'm looking forward to working with them more in the future.</p>
  </article>
  <div class="divider"></div>
  <article class="review" style="left:640px">
    <div class="avatar" role="img" aria-label="Reviewer portrait"></div>
    <div class="who">Maintenance Client - Devon R.</div>
    <div class="stars"><span class="g"></span>★★★★★</div>
    <div class="quote">&rdquo;</div>
    <p>I was surprised that Steadwell Heating and Air actually reached out to me after six months for my no charge follow up visit. I couldn't be happier with this company. On time service as well as professional and very efficient. Thanks again and we will see you in March for my next annual maintenance.</p>
  </article>
</section>

<section>
  <div class="contact-bg" role="img" aria-label="Blurred street backdrop"></div>
  <div class="ph van" role="img" aria-label="Black company service van with flame graphics and phone number 555.014.2290"></div>
  <div class="tab"></div>
  <form class="form">
    <h2>Get In <span class="accent">Touch With Us</span></h2>
    <div class="field" style="top:150px">Full Name<span>&#9679;</span></div>
    <div class="field" style="top:215px">Email Address<span>&#9993;</span></div>
    <div class="field" style="top:283px">Phone Number<span>&#9742;</span></div>
    <div class="field" style="top:352px">Choose a Service<span>&#9636;</span></div>
    <div class="field" style="top:420px">Message<span>&#9636;</span></div>
    <span class="btn">Submit Now</span>
  </form>
</section>

<section class="brands">
  <h2>Major HVAC Equipment<br><span class="accent">BrandsWe're Partnered With</span></h2>
  <div class="brand norvale"><i style="background:#bbb"></i>NORVALE</div>
  <div class="brand kestrel"><i style="background:#d0312d"></i>Kestrel</div>
  <div class="brand brightline"><i style="background:#c8272c;border-radius:6px;width:30px;height:30px"></i>Brightline</div>
  <div class="brand halvor"><i style="background:#333;border-radius:6px"></i>HALVOR</div>
  <div class="brand teloric"><i style="background:#e3262b"></i>TELORIC</div>
</section>

<footer>
  <svg class="footer" width="1200" height="430" viewBox="0 0 1200 430">
    <path d="M0 80 Q600 -10 1200 80 L1200 430 L0 430Z" fill="#0d1424"/>
    <path d="M180 48 Q600 -12 1020 48" fill="none" stroke="#29a3dd" stroke-width="8" stroke-linecap="round"/>
  </svg>
  <div class="f-logo"><div class="dot"></div><div class="name">STEADWELL</div><div class="social"></div></div>
  <div class="f-col" style="left:423px"><h4>Quick Links</h4><ul><li>Home</li><li>About Us</li><li>Services</li><li>Reviews</li><li>Contact Us</li></ul></div>
  <div class="f-col" style="left:585px"><h4>Contact Info</h4>
    <div class="ci"><b></b>(555) 014-2290</div>
    <div class="ci"><b></b>hello@steadwellhvac.com</div>
    <div class="ci"><b></b>Mon - Fri&nbsp; 7:00am - 6:00pm</div>
    <div class="ci"><b></b>Saturday&nbsp; 8:00am - 3:00pm</div>
    <div class="ci"><b></b>Sunday&nbsp; Appointment Only</div>
  </div>
  <div class="f-col" style="left:860px"><h4>Service Areas</h4><ul><li>Charleston</li><li>Mount Pleasant</li><li>Folly Beach</li><li>Summerville</li><li>Isle of Palms</li></ul></div>
  <div class="f-col" style="left:993px;top:4660px"><ul><li>North Charleston</li><li>Sullivan's Island</li><li>Goose Creek</li><li>James Island</li><li>Johns Island</li></ul></div>
  <div class="chat"><svg width="26" height="24" viewBox="0 0 26 24"><path d="M3 3h20v14H10l-6 5v-5H3z" fill="#3F7ED6"/></svg></div>
  <div class="f-rule"></div>
  <div class="copy">&copy; 2025 Steadwell Heating and air. All rights reserved.</div>
</footer>

</body>
</html>
```